Postcard Flyer For Plumbing Company

We are a p[professional plumbing company in NSW that carry out plumbing, electrical and hot water system work.
i want to send a postcard size flyer 105mm x 148mm to our clients to offer $xx off their next job they book with us.
The front of the flyer needs to say.... Feel The Love WIth $35 Off your Next Job. It needs to include a section where their name and postal address can go (74mm W x 24mm H) on the left hand side of the bottom of the flyer - refer attached example.
The other side of the flyer needs to have a section for text, the offer ($35 or $xx what they get off their next job) and also can use the tag line... Call 1 Number for The Best In 3 Trades - Plumbing, Hot Water & Electrical.
Plumbing, hot water and electrical pictures/icons can be used.
I want the flyer to stand out, use the corporate colours and be modern whilst letting them know that they can use this voucher on their next job.
Refer attachments.

Target Market(s)

Homeowners and our existing clients

Industry/Entity Type

Plumbing

Font styles to use
Serif

Colors
0255a3
ec1f27
ffffff
d3d3d3

Requirements
Must have
• Corporate colours and logos
• Red Colour:
• C=0
• M=100
• Y=100
• K=0
• Blue Colour
• C= 100
• M=66
• Y=0
• K=2
• Grey Colour
• C= 26
• M=21
• Y=19
• K=0
Nice to have
• predominately white background
Should not have
• Black background and lots of black.

```html
<!DOCTYPE html>
<html lang="en">
<head>
<meta charset="UTF-8">
<title>Harbor Contracting – $35 Off Postcard</title>
<link rel="stylesheet" href="https://fonts.googleapis.com/css2?family=Lato:wght@400;700&family=Lobster&display=swap">
<style>
  :root {
    --brand-blue: #0255a3;
    --brand-red: #ec1f27;
    --sky-blue: #5aabf2;
    --white: #ffffff;
    --stage-grey: #ebebeb;
    --ink: #2b2b2b;
    --tile-plumbing: #8a8784;
    --tile-electrical: #a5622c;
    --tile-hotwater: #8e8a84;
  }
  html, body {
    margin: 0;
    padding: 0;
    width: 1200px;
    height: 1200px;
    overflow: hidden;
    background: var(--stage-grey);
  }
  .postcard {
    position: absolute;
    left: 236px;
    top: 86px;
    width: 730px;
    height: 1030px;
    background: var(--white);
    box-shadow: 0 4px 14px rgba(0, 0, 0, 0.18);
  }
  .postcard svg {
    display: block;
    width: 100%;
    height: 100%;
  }
  .brand-name { font-family: "Lato", sans-serif; font-weight: 700; fill: var(--brand-blue); }
  .brand-services { font-family: "Lato", sans-serif; font-weight: 700; fill: #1e1e1e; }
  .headline-script { font-family: "Lobster", cursive; fill: var(--brand-red); }
  .offer-amount { font-family: "Lato", sans-serif; font-weight: 700; fill: var(--white); }
  .offer-subline { font-family: "Lato", sans-serif; font-weight: 400; fill: var(--ink); }
  .body-copy { font-family: "Lato", sans-serif; font-weight: 400; fill: var(--ink); }
  .service-label { font-family: "Lato", sans-serif; font-weight: 400; fill: var(--white); }
  .address-panel { fill: var(--white); stroke: #222; stroke-width: 3; }
</style>
</head>
<body>
<main class="postcard">
  <svg viewBox="0 0 912 1287" xmlns="http://www.w3.org/2000/svg">
    <!-- header field -->
    <path class="header-field" fill="var(--sky-blue)"
      d="M0,0 H762 L912,125 V612 C620,570 400,645 120,655 L75,523 L0,515 Z"/>
    <!-- left corner blocks -->
    <polygon fill="var(--white)" points="0,515 75,523 125,652 0,633"/>
    <polygon fill="var(--brand-blue)" points="0,633 125,652 48,762 0,757"/>
    <!-- wave bands -->
    <path fill="var(--brand-blue)"
      d="M120,655 C400,645 620,570 912,612 V680 C780,612 560,612 120,658 Z"/>
    <path fill="none" stroke="var(--brand-red)" stroke-width="5"
      d="M120,655 C400,645 620,570 912,612"/>
    <!-- bottom corner accents -->
    <polygon fill="var(--brand-red)" points="0,1142 0,1287 130,1287"/>
    <polygon fill="var(--brand-blue)" points="912,1047 881,1232 912,1257"/>

    <!-- brand -->
    <text class="brand-name" x="456" y="150" font-size="44" text-anchor="middle">Harbor Contracting</text>
    <text class="brand-services" x="470" y="198" font-size="18" text-anchor="middle">Plumbing • Electrical • Hot Water</text>

    <!-- headline -->
    <text class="headline-script" x="440" y="338" font-size="122" text-anchor="middle">feel the Love</text>
    <polygon fill="var(--brand-blue)" points="150,370 767,370 745,422 767,474 127,474 148,422"/>
    <text class="offer-amount" x="440" y="452" font-size="86" text-anchor="middle">with $35 Off</text>
    <text class="offer-subline" x="450" y="541" font-size="62" text-anchor="middle">ON YOUR NEXT JOB</text>

    <!-- intro copy -->
    <text class="body-copy" font-size="23" text-anchor="middle">
      <tspan x="451" y="694">Lorem Ipsum is simply dummy text of the printing and</tspan>
      <tspan x="451" y="721">typesetting industry. Lorem Ipsum has been the industry's</tspan>
      <tspan x="451" y="749">standard dummy text ever since the 1500s,</tspan>
    </text>

    <!-- service tiles -->
    <g class="service-tile">
      <polygon role="img" aria-label="Photo of a plumber fitting a kitchen tap" fill="var(--tile-plumbing)"
        points="150,789 286,789 327,872 276,954 160,954 109,872"/>
      <polygon fill="var(--brand-blue)" points="126,954 321,954 312,970 321,987 118,987 126,970"/>
      <text class="service-label" x="219" y="980" font-size="24" text-anchor="middle">PLUMBING</text>
    </g>
    <g class="service-tile">
      <polygon role="img" aria-label="Photo of a light bulb on a wooden table" fill="var(--tile-electrical)"
        points="391,789 527,789 568,872 517,954 401,954 350,872"/>
      <polygon fill="var(--brand-blue)" points="365,954 560,954 551,970 560,987 357,987 365,970"/>
      <text class="service-label" x="462" y="980" font-size="24" text-anchor="middle">ELECTRICAL</text>
    </g>
    <g class="service-tile">
      <polygon role="img" aria-label="Photo of water flowing from a sink spout" fill="var(--tile-hotwater)"
        points="632,789 768,789 809,872 758,954 642,954 591,872"/>
      <polygon fill="var(--brand-blue)" points="606,954 801,954 792,970 801,987 598,987 606,970"/>
      <text class="service-label" x="701" y="980" font-size="24" text-anchor="middle">HOT WATER</text>
    </g>

    <!-- recipient address area -->
    <rect class="address-panel" x="135" y="1031" width="642" height="207"/>
  </svg>
</main>
</body>
</html>
```